Organic Sunscreen Business "VelloBloom" Needs Package Design

Our company VelloBloom, manufactures an anti-ageing SPF 15 sunscreen product.

We specialise in the world's most rare and luxury organic anti-ageing ingredients.

We require an attractive package design for a 2.5 oz/75 ml squeezy bottle with box design, a few examples of similar examples which we like are attached.

We have a logo, barcode and graphic, which has been uploaded, and the bottle is to convey the message of wealth and luxury as well as organic sunscreen, we would prefer the package to be colourful and creative in order to sell.

I have included 2 rough sketches of the basic elements and layout of the design. And the box is to be similar to the bottle but to contain an extra caption.

Also, the sketch is only for a guide on how I would like the package, i.e. the labels and graphics can be in different positions/layouts thanks. And any additional creative images, text or fonts would be considered.
Updates

Industry/Entity Type

Business

Requirements
Must have
• FRONT of Bottle:
• LABEL 1: Logo (attached)
• LABEL 2:
• SPF 15
• Non-Nano
• Technology
• 100% Organic
• Paraben Free
• LABEL 3: (Larger/higher emphasis than Label 2)
• Anti-Ageing
• Moisturiser
• BACK of Bottle:
• Introduction: (For me to add personally at later date)
• Warnings: For external use only. Do not use on damaged or broken skin. Stop use and ask a doctor if rash occurs. When using this product keep out of eyes. Rinse with water to remove.
• Directions: Shake well before use. Apply liberally 15 minutes before sun exposure. Use a water resistant sunscreen if swimming or sweating. Reapply at least every 2 hours. Children under 6 months: Ask a doctor.
• Active Ingredient: Non-Nano Zinc Oxide (6%)
• Also contains: (For me to add personally at later date)
• Barcode: (image attached)
• Contact: www.vellobloom-example.com.au
• 2.5oz/7ml e
• BOX:
• Same as bottle, but one side will contain the caption:
• "7 NATURAL WONDERS IN 1" (In a creative style)
Nice to have
• Additional Text/Images/Fonts relating to the subject(s)
• Most creative design will be the winner.

```html
<!DOCTYPE html>
<html lang="en">
<head>
<meta charset="utf-8">
<title>VelloBloom Anti-Ageing Moisturiser SPF 15 – Box and Tube</title>
<link rel="stylesheet" href="https://fonts.googleapis.com/css2?family=Cinzel:wght@400;600;700&display=swap">
<style>
  :root {
    --backdrop-light: #cfa9aa;
    --backdrop-dark: #a98082;
    --panel-white: #f4f7fa;
    --pattern-tint: #e3edf6;
    --brand-blue: #2a74b8;
    --deep-blue: #1f5f9e;
    --gold: #c9a24a;
    --sun-orange: #f5a93a;
    --cap-orange: #f08a12;
    --cap-light: #ffb347;
    --scene-sky: #eef3f7;
    --scene-sand: #e2a54a;
    --scene-green: #5f7f34;
    --scene-water: #4f93cf;
  }
  * { box-sizing: border-box; margin: 0; padding: 0; }
  html, body { width: 1200px; height: 780px; overflow: hidden; }
  body {
    position: relative;
    background: radial-gradient(ellipse at 50% 40%, var(--backdrop-light), var(--backdrop-dark));
    font-family: "Cinzel", serif;
    color: var(--brand-blue);
  }
  .panel {
    position: absolute;
    background: linear-gradient(var(--panel-white), var(--pattern-tint));
    box-shadow: 0 6px 18px rgba(80, 40, 45, 0.25);
    overflow: hidden;
  }
  .box-side { left: 300px; top: 150px; width: 180px; height: 480px; }
  .box-front { left: 480px; top: 150px; width: 240px; height: 480px; border-left: 1px solid #d6dde4; }
  .tube-label { left: 780px; top: 170px; width: 250px; height: 380px; }
  .tube-cap {
    position: absolute; left: 780px; top: 550px; width: 250px; height: 80px;
    background: linear-gradient(90deg, var(--cap-orange), var(--cap-light) 45%, var(--cap-orange));
    border-radius: 0 0 8px 8px;
    box-shadow: 0 6px 18px rgba(80, 40, 45, 0.25);
  }

  .wonders-badge {
    position: absolute; left: 15px; top: 40px; width: 150px; height: 150px;
    border-radius: 50%; background: var(--sun-orange);
    display: flex; flex-direction: column; align-items: center; justify-content: center;
    color: #fff; text-align: center; font-size: 19px; line-height: 1.15; font-weight: 600;
  }

  .brand {
    position: absolute; left: 0; right: 0; text-align: center;
    display: flex; flex-direction: column; align-items: center; gap: 6px;
    color: var(--gold);
  }
  .brand-mark { width: 34px; height: 34px; border-radius: 50%; border: 2px solid var(--gold); }
  .brand-name { font-size: 15px; font-weight: 600; }
  .box-front .brand { top: 40px; }
  .tube-label .brand { top: 22px; }
  .tube-label .brand-mark { width: 26px; height: 26px; }
  .tube-label .brand-name { font-size: 12px; }

  .product-title {
    position: absolute; left: 0; right: 0; text-align: center;
    color: var(--brand-blue); font-weight: 600;
  }
  .product-title span { display: block; }
  .sun-dot {
    width: 22px; height: 22px; margin: 6px auto; border-radius: 50%;
    background: radial-gradient(circle, var(--sun-orange) 45%, rgba(245,169,58,0.2) 70%, transparent 72%);
  }
  .box-front .product-title { top: 125px; font-size: 17px; }
  .tube-label .product-title { top: 88px; font-size: 13px; }
  .tube-label .sun-dot { width: 18px; height: 18px; }

  .scene {
    position: absolute; left: 0; right: 0;
    background: linear-gradient(180deg, var(--scene-sky) 0%, var(--scene-sand) 22%, var(--scene-sand) 40%, var(--scene-green) 48%, var(--scene-green) 55%, var(--scene-water) 62%, #a9cbe8 100%);
    opacity: 0.85;
  }
  .box-side .scene, .box-front .scene { top: 210px; height: 130px; }
  .tube-label .scene { top: 180px; height: 70px; }

  .rule { position: absolute; left: 0; right: 0; height: 3px; background: var(--brand-blue); }
  .box-side .rule-top { top: 395px; }
  .box-side .rule-bottom { top: 455px; }
  .blank-label { position: absolute; left: 0; right: 0; top: 400px; height: 52px; background: #fff; }

  .seal { position: absolute; left: 50%; transform: translateX(-50%); }
  .box-front .seal { top: 370px; width: 230px; height: 100px; }
  .tube-label .seal { top: 262px; width: 240px; height: 105px; }
  .seal text { font-family: "Cinzel", serif; }
</style>
</head>
<body>

  <section class="panel box-side" aria-label="Box side panel">
    <div class="wonders-badge"><span>7</span><span>Natural</span><span>Wonders</span><span>in 1</span></div>
    <div class="scene" role="img" aria-label="Sketched pyramids beside green palms over blue water"></div>
    <div class="rule rule-top"></div>
    <div class="blank-label"></div>
    <div class="rule rule-bottom"></div>
  </section>

  <section class="panel box-front" aria-label="Box front panel">
    <div class="brand"><div class="brand-mark"></div><div class="brand-name">VelloBloom</div></div>
    <div class="product-title"><span>Anti-Ageing</span><div class="sun-dot"></div><span>Moisturiser</span></div>
    <div class="scene" role="img" aria-label="Sketched pyramids beside green palms over blue water"></div>
    <svg class="seal" viewBox="0 0 230 100" aria-label="SPF 15, Non-Nano Technology, 100% Organic, Paraben Free">
      <defs>
        <path id="arc-top-box" d="M75 52 A40 40 0 0 1 155 52"/>
        <path id="arc-bottom-box" d="M72 52 A43 43 0 0 0 158 52"/>
      </defs>
      <circle cx="115" cy="52" r="46" fill="#fff" stroke="#2a74b8" stroke-width="2"/>
      <circle cx="115" cy="52" r="24" fill="#2a74b8"/>
      <text x="115" y="58" text-anchor="middle" font-size="14" font-weight="700" fill="#f5a93a">SPF 15</text>
      <text font-size="9" font-weight="700" fill="#2a74b8"><textPath href="#arc-top-box" startOffset="50%" text-anchor="middle">NON-NANO</textPath></text>
      <text font-size="9" font-weight="700" fill="#2a74b8"><textPath href="#arc-bottom-box" startOffset="50%" text-anchor="middle">TECHNOLOGY</textPath></text>
      <text x="36" y="50" text-anchor="middle" font-size="9" fill="#2a74b8">100%</text>
      <text x="36" y="61" text-anchor="middle" font-size="9" fill="#2a74b8">ORGANIC</text>
      <text x="194" y="50" text-anchor="middle" font-size="9" fill="#2a74b8">PARABEN</text>
      <text x="194" y="61" text-anchor="middle" font-size="9" fill="#2a74b8">FREE</text>
    </svg>
  </section>

  <section class="panel tube-label" aria-label="Tube front label">
    <div class="brand"><div class="brand-mark"></div><div class="brand-name">VelloBloom</div></div>
    <div class="product-title"><span>Anti-Ageing</span><div class="sun-dot"></div><span>Moisturiser</span></div>
    <div class="scene" role="img" aria-label="Sketched pyramids beside green palms over blue water"></div>
    <svg class="seal" viewBox="0 0 240 105" aria-label="SPF 15, Non-Nano Technology, 100% Organic, Paraben Free">
      <defs>
        <path id="arc-top-tube" d="M78 55 A42 42 0 0 1 162 55"/>
        <path id="arc-bottom-tube" d="M75 55 A45 45 0 0 0 165 55"/>
      </defs>
      <circle cx="120" cy="55" r="48" fill="#fff" stroke="#2a74b8" stroke-width="2"/>
      <circle cx="120" cy="55" r="25" fill="#2a74b8"/>
      <text x="120" y="61" text-anchor="middle" font-size="14" font-weight="700" fill="#f5a93a">SPF 15</text>
      <text font-size="9" font-weight="700" fill="#2a74b8"><textPath href="#arc-top-tube" startOffset="50%" text-anchor="middle">NON-NANO</textPath></text>
      <text font-size="9" font-weight="700" fill="#2a74b8"><textPath href="#arc-bottom-tube" startOffset="50%" text-anchor="middle">TECHNOLOGY</textPath></text>
      <text x="38" y="53" text-anchor="middle" font-size="9" fill="#2a74b8">100%</text>
      <text x="38" y="64" text-anchor="middle" font-size="9" fill="#2a74b8">ORGANIC</text>
      <text x="202" y="53" text-anchor="middle" font-size="9" fill="#2a74b8">PARABEN</text>
      <text x="202" y="64" text-anchor="middle" font-size="9" fill="#2a74b8">FREE</text>
    </svg>
  </section>
  <div class="tube-cap" aria-hidden="true"></div>

</body>
</html>
```